Rondo Brisk Painting, Eco and Non toxic painting client information brochure.

Rondo brisk painting is a painting company that specialises in eco and non toxic paints. This brochure will be left with the client after the initial meeting to explain about my business and hopefully win the job. By reading the text i have provided (see attachment) you can get a better understanding of what we do.
The brochure should be fresh and clean looking, complimenting the Rondo Brisk Painting logo and the text provided.
This will be printed onto a recycled paper.
Text and font must clear and easy to read.

Please have a look at my web page. I will be redoing this soon as well but this will give you some ideas of where I'm at.

Would like some picture but not sure what.
I have attached some pics but they don't have to be use

Hi peeps,

Thanks for all the great designs and sorry i haven't got back to you sooner.
been a bit busy.
Tomorrow i hope to be able to sit down and have a good look at what everybody has done.
Thanks again i really appreciate the effort.

kind regards gerald 

hi designers,

Just sat down and had a good look at the designs sent in and there are some crackers.
Its going to be very difficult to choose. I have only 1 day left before it closes so ill wait till then to see if there are any more submissions come in then ill get back to everybody.
Thanks again for your time and effort.

kind regards gerald 

Hi too all you designers that have worked on my project. 

I am always amazed at all the different designs that come through. Super work guys and girls. 
I have narrowed it down to a couple of designs.
Ill be making the decision tonight.
Thanks again to you all and i really appreciate all the hard work.
I will be doing another brochure in the future for more architecture / builder focus and there were a few designs that would work perfectly for this.

Kinds regards gerald  

Target Market(s)

The work we do is mainly residential repaints, family homes
Mostly I am dealing with the wife of the family or female designers/architects

Industry/Entity Type

Painting

Requirements
Must have
• Company logo, either white or black version what ever suits best.
Text that has been provided.
Brochure will be 1 page A 4, folded into 3 parts both sides.
Front page must have logo and
SPECIALSING IN:
NON TOXIC
ECO FRIENDLY &
HEAT REFLECTIVE PAINTS
Phone 041 862 9147
Painting@rondobrisk.biz
www.rondobrisk.biz

```html
<!DOCTYPE html>
<html lang="en">
<head>
<meta charset="utf-8">
<title>Rondo Brisk Painting – Brochure Inner Spread</title>
<link rel="stylesheet" href="https://fonts.googleapis.com/css2?family=Nunito:wght@500;600;700&display=swap">
<style>
  :root {
    --page-bg: #ffffff;
    --band-light: #eef2f6;
    --band-blue: #d3dee8;
    --panel-blue: #d5e0e9;
    --panel-blue-deep: #c8d6e2;
    --panel-text-bg: #e3eaf0;
    --panel-white: #ffffff;
    --panel-grey: #e4e4e4;
    --heading-red: #b8302f;
    --body-ink: #1d1d1d;
  }
  * { box-sizing: border-box; margin: 0; padding: 0; }
  html, body { width: 1200px; height: 900px; overflow: hidden; background: var(--page-bg); }
  .canvas {
    position: relative; width: 1200px; height: 900px; overflow: hidden;
    font-family: "Nunito", "Helvetica Neue", Arial, sans-serif; color: var(--body-ink);
  }
  .band { position: absolute; left: 40px; width: 1135px; }
  .band--top-light { top: 0; height: 28px; background: linear-gradient(#f6f8fa, #e6ecf1); }
  .band--top-blue { top: 28px; height: 52px; background: linear-gradient(#dbe4ec, #cfdbe5 60%, #e9eef3); }
  .band--bottom-light { top: 820px; height: 45px; background: linear-gradient(#e6ecf1, #f8fafb 50%, #e2e9ef); }
  .band--bottom-blue { top: 865px; height: 35px; background: linear-gradient(#d6e0e9, #cbd8e3); }

  .panel { position: absolute; top: 80px; height: 740px; }
  .panel--business { left: 40px; width: 390px; background: var(--panel-blue); }
  .panel--owner { left: 430px; width: 363px; background: linear-gradient(var(--panel-white) 0, var(--panel-white) 313px, var(--panel-grey) 313px, #ececec 100%); }
  .panel--showcase { left: 793px; width: 382px; background: linear-gradient(var(--panel-blue) 0, var(--panel-blue) 373px, var(--panel-blue-deep) 373px); }

  .text-block--business {
    position: absolute; left: 0; top: 357px; width: 390px; height: 383px;
    background: linear-gradient(#dfe6ed, var(--panel-text-bg) 40%, #e8edf2);
  }

  .photo { position: absolute; }
  .photo--red-sofa { left: 0; top: 20px; width: 370px; height: 315px;
    background: linear-gradient(#5a5c5f, #46484b 70%, #2b2b2c 79%, #1b0f0f 82%, #3a1212 100%); }
  .photo--green-room { left: 18px; top: 18px; width: 327px; height: 275px;
    background: linear-gradient(#d2dc44, #c4d03a 75%, #9aa47a 78%, #aeb39c 100%); }
  .photo--ochre-wall { left: 15px; top: 20px; width: 367px; height: 333px;
    background: linear-gradient(#7c6842, #6e5b37 76%, #e9eaea 79%, #f7f7f6 100%); }
  .photo--slate-wall { left: 23px; top: 392px; width: 359px; height: 328px;
    background: linear-gradient(#7790a0, #6a8493 82%, #a27a4c 84%, #8c6640 100%); }

  .heading {
    position: absolute; color: var(--heading-red); font-weight: 600;
    font-size: 20px; letter-spacing: 0.4px; text-align: center; white-space: nowrap;
  }
  .body-copy {
    position: absolute; font-size: 11px; font-weight: 700; line-height: 15.8px;
    text-align: justify; letter-spacing: 0.1px;
  }

  .heading--business { left: 0; width: 390px; top: 411px; }
  .body-copy--business { left: 40px; width: 330px; top: 460px; }

  .heading--owner { left: 0; width: 363px; top: 328px; }
  .body-copy--owner { left: 41px; width: 292px; top: 382px; }
  .heading--hiring { left: 0; width: 363px; top: 452px; }
  .body-copy--hiring { left: 48px; width: 255px; top: 493px; text-align: left; }
  .heading--green { left: 0; width: 330px; top: 586px; }
  .body-copy--green { left: 55px; width: 247px; top: 619px; }
</style>
</head>
<body>
<div class="canvas">
  <div class="band band--top-light"></div>
  <div class="band band--top-blue"></div>

  <section class="panel panel--business">
    <div class="photo photo--red-sofa" role="img" aria-label="Living room with a dark grey wall, a red leather sofa and a red vase on a glossy floor"></div>
    <div class="text-block--business"></div>
    <h2 class="heading heading--business">ABOUT THE BUSINESS</h2>
    <p class="body-copy body-copy--business">At Rondo Brisk Painting we provide a high-quality service and exceptional craftsmanship for both domestic and commercial projects. We are proud to say we are making our work practices and business support processes more sustainable. We want to be sure we are doing our part to reduce our carbon footprint. We take the time to research alternative eco painting products and processes. We can also provide you with information about the products and why we use them. All our jobs are professionally finished utilising only the best tools and products available. We aim to limit the interruption to clients and their families as a result of our work; safety is paramount. We make sure that you are satisfied with the work done and will communicate with you throughout the job. Rondo Brisk Painting is dedicated to learning, understanding and implementing new products and techniques that will be safer for the environment and your family. All this is done at a competitive price.</p>
  </section>

  <section class="panel panel--owner">
    <div class="photo photo--green-room" role="img" aria-label="Lime green painted wall with a green sofa, pendant lamp and white cube shelving"></div>
    <h2 class="heading heading--owner">ABOUT THE OWNER</h2>
    <p class="body-copy body-copy--owner">Gerald Brisk has been painting for over 20 years. He is an accredited Green Painter and is often called upon by architects and builders to provide advice on sustainable products and methods.</p>
    <h2 class="heading heading--hiring">HIRING A PROFESSIONAL</h2>
    <p class="body-copy body-copy--hiring">Hiring a professional painter is never an easy decision and one not to be taken lightly. Painting is a highly skilled trade and it takes considerable experience and<br>expertise to obtain a high quality finish.</p>
    <h2 class="heading heading--green">GOING GREEN</h2>
    <p class="body-copy body-copy--green">We can help you make smart decisions about creating a better environment and further minimizing any risk for your family and the spaces we live in. This can be<br>achieved reducing the amount of VOCs (volatile organic compounds) by selecting the correct products.</p>
  </section>

  <section class="panel panel--showcase">
    <div class="photo photo--ochre-wall" role="img" aria-label="Textured ochre brown wall with white zigzag shelf, yellow vases and a white sofa"></div>
    <div class="photo photo--slate-wall" role="img" aria-label="Slate blue textured wall with a dark leather sofa, blue vase and timber floor"></div>
  </section>

  <div class="band band--bottom-light"></div>
  <div class="band band--bottom-blue"></div>
</div>
</body>
</html>
```